Tandem Tots Flyer - 2 WEEK FREE TRIAL

FLYER - We need a 1 page DL flyer with images and text. Have flyer in landscape

OFFER - 2 WEEK FREE TRIAL

HOW TO GET
Book online now at www.tandemtotsplay.com.au/booking

TAG -Where Kids are Champions

PRIZE
Chance to win Full Term of 10 weekly sessions

GIVEAWAYS
Chance to get giveaways such as tickets to games, footballs or other great offers.

LOGO - Attached

Target Market(s)

Parents of children from 5 to 16

Industry/Entity Type

Fitness

Colors
0455a3
ffc214

Requirements
Must have
• Attraction for parents to go online and sign up their kids
Should not have
• Not dull or boring

```html
<!DOCTYPE html>
<html lang="en">
<head>
<meta charset="utf-8">
<title>Tandem Tots – 2-Week Free Trial</title>
<link href="https://fonts.googleapis.com/css2?family=Alfa+Slab+One&family=Archivo+Black&family=Open+Sans:wght@400;700;800&display=swap" rel="stylesheet">
<style>
  :root {
    --brand-blue: #0455a3;
    --brand-yellow: #ffc214;
    --headline-red: #d8231f;
    --heading-green: #1f8d2b;
    --ink: #2a2a2a;
    --white: #ffffff;
    --scene-top: #2a2c30;
    --scene-bottom: #5f8a3a;
    --photo-fill: #8c7a6e;
    --object-fill: #b9b3a8;
  }
  * { margin: 0; padding: 0; box-sizing: border-box; }
  html, body { width: 1200px; height: 571px; overflow: hidden; background: var(--white); }
  .flyer {
    position: relative; width: 1200px; height: 571px; overflow: hidden;
    font-family: "Open Sans", Arial, sans-serif;
  }
  .stadium-scene {
    position: absolute; left: 0; top: 0; width: 1200px; height: 505px;
    background: linear-gradient(180deg, var(--scene-top) 0%, var(--scene-bottom) 100%);
  }
  .player-photo {
    position: absolute; left: 770px; top: 15px; width: 205px; height: 480px;
    background: var(--photo-fill);
  }
  .balls-photo {
    position: absolute; left: 968px; top: 388px; width: 218px; height: 104px;
    background: var(--object-fill);
  }
  .headline { position: absolute; left: 0; top: 0; font-family: "Alfa Slab One", Georgia, serif; color: var(--brand-yellow); font-weight: 400; }
  .headline span {
    position: absolute; white-space: nowrap; line-height: 1;
    -webkit-text-stroke: 3px var(--headline-red); paint-order: stroke fill;
  }
  .headline .where { left: 210px; top: 132px; font-size: 32px; transform: rotate(-90deg); transform-origin: left top; }
  .headline .kids { left: 258px; top: 12px; font-size: 112px; }
  .headline .are { left: 352px; top: 118px; font-size: 46px; }
  .headline .champions { left: 98px; top: 150px; font-size: 112px; letter-spacing: -2px; }
  .offer {
    position: absolute; left: 75px; top: 284px; font-family: "Archivo Black", Arial, sans-serif;
    font-size: 44px; line-height: 56px; color: var(--brand-blue); white-space: nowrap;
    -webkit-text-stroke: 4px var(--white); paint-order: stroke fill;
  }
  .perk { position: absolute; text-align: center; color: var(--ink); font-weight: 700; font-size: 18px; line-height: 26px; }
  .perk h2 {
    font-size: 18px; font-weight: 800; color: var(--heading-green); text-decoration: underline;
    line-height: 22px; margin-bottom: 4px;
  }
  .perk-prize { left: 55px; top: 372px; width: 300px; }
  .perk-giveaways { left: 415px; top: 358px; width: 320px; }
  .program-badges { position: absolute; left: 1020px; top: 55px; display: flex; flex-direction: column; gap: 90px; }
  .program-badge { display: flex; align-items: center; gap: 8px; }
  .program-badge .dot { width: 16px; height: 16px; border-radius: 50%; background: var(--brand-blue); }
  .program-badge .name { font-weight: 800; font-size: 18px; color: var(--brand-yellow); white-space: nowrap; }
  .footer-band {
    position: absolute; left: 0; bottom: 0; width: 1200px; height: 66px; background: var(--brand-blue);
    color: var(--brand-yellow); font-size: 22px; letter-spacing: 1.6px; line-height: 66px;
  }
  .footer-band span { position: absolute; top: 0; white-space: nowrap; }
  .footer-band .booking { left: 40px; }
  .footer-band .divider { left: 772px; color: var(--white); font-size: 26px; }
  .footer-band .site { left: 810px; }
</style>
</head>
<body>
<main class="flyer">
  <div class="stadium-scene" role="img" aria-label="Floodlit football stadium at dusk with a green pitch"></div>
  <div class="player-photo" role="img" aria-label="Young player in sports kit seen from behind, hands on hips"></div>
  <div class="balls-photo" role="img" aria-label="Soccer ball, football and baseball on the grass"></div>

  <h1 class="headline">
    <span class="where">Where</span>
    <span class="kids">Kids</span>
    <span class="are">are</span>
    <span class="champions">Champions</span>
  </h1>

  <p class="offer">OFFER 2-WEEK FREE TRIAL</p>

  <section class="perk perk-prize">
    <h2>PRIZE</h2>
    <p>Chance to win Full Term of<br>10 weekly sessions.</p>
  </section>

  <section class="perk perk-giveaways">
    <h2>GIVEAWAYS</h2>
    <p>Chance to get giveaways such<br>as tickets to games, footballs or<br>other great offers.</p>
  </section>

  <div class="program-badges">
    <div class="program-badge"><span class="dot"></span><span class="name">Tandem Tots</span></div>
    <div class="program-badge"><span class="dot"></span><span class="name">Tandem Tots</span></div>
    <div class="program-badge"><span class="dot"></span><span class="name">Tandem Tots</span></div>
  </div>

  <footer class="footer-band">
    <span class="booking">Book online now at www.tandemtotsplay.com.au/booking</span>
    <span class="divider">|</span>
    <span class="site">www.tandemtotsplay.com.au</span>
  </footer>
</main>
</body>
</html>
```